Health - Still Meadow Project

I am running a new Still Meadow Conference that will have meditation, mediums and healers - this is a first time conference. However the conference is aimed at mainstream 'normal' people. The 'normal' people, don't want to hear or see words like Tantra, Prana, Angels, etc, but they have problems that can be alleviated through these mediums. The design should communicate light, soothing, comforting, healing. I would like a web design for a single page that can be used as a landing page for the conference registration. I also need a logo and a flyer that can be made into posters A4 or A3 posters. I need to be able to edit all documents as there will be changes in the program through time. I have attached the initial agenda. This conference will be held in Victoria, Australia.
Target Market(s)
Mums and grandmas
Industry/Entity Type
Health And Wellness
Number of Pages Required
1 page

```html
<!DOCTYPE html>
<html lang="en">
<head>
<meta charset="utf-8">
<title>Still Meadow Conference</title>
<link rel="stylesheet" href="https://fonts.googleapis.com/css2?family=Open+Sans:wght@300;400;600;700&family=Oswald:wght@700&display=swap">
<style>
:root{
  --green:#3a8b34;
  --yellow:#f6cd0c;
  --gold:#f7d21f;
  --white:#ffffff;
  --ink:#2b2b2b;
  --dark:#424242;
  --footer:#f1f1f1;
  --hero-a:#2fb7a8;
  --hero-b:#f4e58a;
}
*{box-sizing:border-box;margin:0;padding:0}
html,body{width:1200px;height:3340px;overflow:hidden}
body{font-family:"Open Sans",Arial,sans-serif;color:var(--white);background:var(--white)}

.hero{position:relative;height:659px;overflow:hidden}
.hero-photo{position:absolute;inset:0;background:
  radial-gradient(ellipse at 68% 30%,#fff8d8 0%,rgba(255,248,216,0) 45%),
  linear-gradient(120deg,var(--hero-a) 0%,#8fd3b0 45%,var(--hero-b) 75%,#e9c76b 100%)}
.topbar{position:absolute;top:0;left:0;right:0;height:116px;background:rgba(120,120,100,.45);display:flex;align-items:center;justify-content:space-between;padding:0 100px 0 140px}
.brand{font-size:34px;font-weight:300;color:var(--white);letter-spacing:.5px}
.event-date{font-size:24px;font-weight:600;color:var(--white)}
.event-date sup{font-size:14px}
.hero-copy{position:absolute;left:142px;top:222px;text-transform:uppercase;line-height:1}
.hero-copy .l1{font-size:64px;color:var(--gold);font-weight:400}
.hero-copy .l2{font-size:38px;color:var(--white);font-weight:300;margin-top:6px}
.hero-copy .l2 b{font-size:50px;font-weight:300}
.hero-copy .l3{font-size:50px;color:var(--white);font-weight:300;margin-top:4px}
.hero-copy .l4{font-size:72px;color:var(--gold);font-weight:400;margin-top:4px}
.hero-copy .sub{font-size:20px;font-weight:700;color:var(--white);margin-top:18px;line-height:1.35}
.arrow{position:absolute;top:380px;width:30px;height:40px}
.arrow.left{left:78px}.arrow.right{right:78px}

.session{position:relative;padding:0 142px}
.session.green{background:var(--green)}
.session.yellow{background:var(--yellow)}
.session h2{font-size:31px;font-weight:400;text-transform:uppercase;padding-top:40px;margin-bottom:24px;letter-spacing:-.3px}
.green h2{color:var(--gold)}
.yellow h2{color:var(--white)}
.session-body{display:flex;gap:24px;align-items:flex-start}
.yellow .session-body{gap:40px}
.portrait{flex:0 0 152px;height:176px;border:3px solid #e8e8e8;background:linear-gradient(160deg,#c9b7a4,#8c7867)}
.session p{font-size:12.5px;line-height:22px;color:var(--white)}
.yellow p{color:var(--ink)}
.session p+p{margin-top:16px}
.facilitator{font-size:11.5px;font-weight:700;text-transform:uppercase;margin:20px 0 4px}
.green .facilitator{color:var(--gold)}
.yellow .facilitator{color:var(--ink)}
.time{display:inline-flex;align-items:center;gap:10px;height:44px;padding:0 16px;font-size:18px;margin-top:34px}
.green .time{background:var(--yellow);color:var(--ink);border:2px solid #2a5d26}
.yellow .time{background:var(--green);color:var(--gold)}
.time svg{width:22px;height:22px}

.s1{height:632px}.s2{height:597px}.s3{height:556px}.s4{height:494px}

.contact{height:334px;background:var(--dark);text-align:center;padding-top:40px}
.contact h2{font-family:"Oswald",Impact,sans-serif;font-size:46px;color:var(--gold);letter-spacing:1px}
.contact .rule{width:430px;height:1px;background:#6a6a6a;margin:14px auto 22px}
.contact-row{display:flex;justify-content:center;gap:48px;font-size:19px}
.contact-row span{display:flex;align-items:center;gap:8px}
.contact-row svg{width:26px;height:26px}
.address{margin-top:30px;font-size:19px;line-height:28px}
.address strong{display:block}
.footer{height:68px;background:var(--footer);color:#777;font-size:12px;text-align:center;line-height:68px}
</style>
</head>
<body>

<header class="hero">
  <div class="hero-photo" role="img" aria-label="Photo of a woman with arms outstretched in warm sunlight over a green field"></div>
  <div class="topbar">
    <div class="brand">Still Meadow Conference</div>
    <div class="event-date">Saturday, &nbsp;August &nbsp;20<sup>TH</sup> 2016</div>
  </div>
  <div class="hero-copy">
    <div class="l1">Maecenas</div>
    <div class="l2">Vitae ipsum <b style="color:var(--gold)">Vitae</b></div>
    <div class="l3">Ipsum suscipit,</div>
    <div class="l4">Morbi mattis</div>
    <div class="sub">Integer ligula elit, eleifend quis felis<br>vitae, varius vulputate ipsum.</div>
  </div>
  <svg class="arrow left" viewBox="0 0 30 40"><path d="M22 4 8 20l14 16" fill="none" stroke="#fff" stroke-width="5"/></svg>
  <svg class="arrow right" viewBox="0 0 30 40"><path d="M8 4l14 16L8 36" fill="none" stroke="#fff" stroke-width="5"/></svg>
</header>

<section class="session green s1">
  <h2>Wild Hairs – Embarking upon the Spiritual Life</h2>
  <div class="session-body">
    <div class="portrait" role="img" aria-label="Portrait photo of facilitator Maren Holloway"></div>
    <div>
      <p>Everyone is searching for love, joy and peace – aren't we? Yet love, joy and peace is already our natural state of being. So how did we come to forget this fundamental Truth? Why are we searching for what we already are? The answers to these questions are rather simple and obvious, but only after we come to understand the nature of the human ego. For too long, the human ego has taken us on a wild goose chase.</p>
      <p>It could take an entire lifetime of study to fully grasp the magnitude of the nature of awakening. In this discussion you will receive a very simple to understand explanation of the journey humanity is undertaking, from conception to enlightenment – and how you can assess where you are on your own journey and keys to unlocking your love, joy and peace.</p>
    </div>
  </div>
  <div class="facilitator">Facilitator: Maren Holloway</div>
  <p>A modern day spiritual facilitator, Maren Holloway takes a fresh and fun approach to redefining spirituality for everyone. Maren's own spiritual awakening propelled her to share what is possible, when one truly commits to transformation. True transformation requires a deep understanding of our mind. Hidden deep within our mind-made stories lies, in waiting, the truth of who we are. Maren is an ordained minister, author, certified clinical hypnotherapist, ministerial counselor, workshop facilitator, speaker and medical intuitive. Her simple techniques and practical tools have helped to transform many lives.</p>
  <div class="time"><svg viewBox="0 0 22 22"><circle cx="11" cy="11" r="9" fill="none" stroke="currentColor" stroke-width="2"/><path d="M6 11h6V6" fill="none" stroke="currentColor" stroke-width="2"/></svg>9:00 – 10:45</div>
</section>

<section class="session yellow s2">
  <h2>Conscious Connection &amp; Living Life Fully</h2>
  <div class="session-body">
    <div>
      <p>We live in a world where most people feel disconnected or 'out of synch' with friends, loved ones and the daily experiences we share with one another. This workshop is designed to offer you a framework for LIVING more consciously, intimately and with greater connection, presence and depth – to ourselves and others. The more we feel connected to ourselves, the more connected we will feel with others. In a time where more and more people are feeling isolated in a busy urban existence, simple practices can foster love, connection and fulfillment. Come &amp; explore simple, facilitated exercises that deepen a heart-felt, authentic and feeling space.</p>
      <div class="facilitator">Facilitator: Tessa Marlow</div>
      <p>With a background in laughter-yoga, dance, coaching, psychology, and life-modelling, Tessa brings authenticity, accessibility, warmth and humour to all she does. She is a nurturing leader and passionate advocate for human beings loving every aspect of themselves - the light and the dark, finding new expansive edges and living life fully. She has facilitated Conscious Connection workshops for women, 7 week Dancing Journeys, and Sacred Self Care gatherings, and an immersive weekend feminine sexual archetype retreat. Tessa is passionate about sharing accessible and powerful practices to cultivate self-connection, intimacy and love.</p>
    </div>
    <div class="portrait" role="img" aria-label="Portrait photo of facilitator Tessa Marlow"></div>
  </div>
  <div class="time"><svg viewBox="0 0 22 22"><circle cx="11" cy="11" r="9" fill="none" stroke="currentColor" stroke-width="2"/><path d="M6 11h6V6" fill="none" stroke="currentColor" stroke-width="2"/></svg>11:00 – 12:45</div>
</section>

<section class="session green s3">
  <h2>The Slow Breath to Freedom</h2>
  <div class="session-body">
    <div class="portrait" role="img" aria-label="Portrait photo of facilitator Owen Castell"></div>
    <div>
      <p>Stress is is one of the number one causes of leading diseases today. The connection between Mind and Body has long since been established by both science and spirituality. This session will guide you through simple meditations, self-inquiry, mindful eating and movement. You will find these tools extremely useful to releasing the stress valve, improving your relationships and managing your day to day life in a more enjoyable, present way.</p>
      <p>Using his highly intuitive skills and the "Open Heart Process" Owen will help you experience your divine nature and harness your individual power – enabling you to live a life in harmony and peace.</p>
      <p>Working largely through breathing, focusing and self-inquiry techniques Owen has discovered we can all be transformed. These approaches help people break through old limiting patterns of behaviour, helping them to make healthy and positive change in their lives.</p>
    </div>
  </div>
  <div class="facilitator">Facilitator: Owen Castell</div>
  <p>Owen has over 35 years of experience in meditation, healing and martial arts. Owen is extremely compassionate and non-judgemental – having suffered and healed many personal challenges common to us all – and works to help you discover your own true happiness and meaning in life</p>
  <div class="time"><svg viewBox="0 0 22 22"><circle cx="11" cy="11" r="9" fill="none" stroke="currentColor" stroke-width="2"/><path d="M6 11h6V6" fill="none" stroke="currentColor" stroke-width="2"/></svg>1:30 – 3:15</div>
</section>

<section class="session yellow s4">
  <h2>Learning to Shine</h2>
  <div class="session-body">
    <div>
      <p>In a world where too often we feel less than our bright, shiny best we can all afford to bring out more of our own natural light to shine for ourselves and others. In this session, Nadia will guide you through ways to connect with your inner SHINE and not only use that to brighten yourself, but to shine your light on others to share in warmth and love that improves all things.</p>
      <div class="facilitator">Facilitator: Nadia Brooke</div>
      <p>A loving mum, devoted wife and shining light on her community, Nadia Brooke shares her wealth of knowledge that you can implement into your everyday life. Showing you how to make your inner light shine brighter. Which can transcend in all areas of your life. Nadia has spent the last 20 years absorbing many aspects of "Spirituality" from her personal journey as a Manager in a five star Hotel to meeting a respected meditation teacher. Gaining knowledge in intuition, Numerology, Tarot, Energy Healing and Mindfulness. Nadia loves to share her "toolbox" with you so that you may also bring more joy into your life and those around you. Shine bright XX</p>
    </div>
    <div class="portrait" role="img" aria-label="Portrait photo of facilitator Nadia Brooke"></div>
  </div>
  <div class="time"><svg viewBox="0 0 22 22"><circle cx="11" cy="11" r="9" fill="none" stroke="currentColor" stroke-width="2"/><path d="M6 11h6V6" fill="none" stroke="currentColor" stroke-width="2"/></svg>3:30 – 5:00PM</div>
</section>

<section class="contact">
  <h2>CONTACT US</h2>
  <div class="rule"></div>
  <div class="contact-row">
    <span><svg viewBox="0 0 26 26"><circle cx="13" cy="13" r="11.5" fill="none" stroke="#f6cd0c" stroke-width="2"/><path d="M9 7l3 3-1.5 2a8 8 0 0 0 4 4l2-1.5 3 3-2 2C12 19 7 14 7 9z" fill="#f6cd0c"/></svg>Phone : <b>555-014-2230</b></span>
    <span><svg viewBox="0 0 26 26"><circle cx="13" cy="13" r="11.5" fill="none" stroke="#f6cd0c" stroke-width="2"/><path d="M9 7l3 3-1.5 2a8 8 0 0 0 4 4l2-1.5 3 3-2 2C12 19 7 14 7 9z" fill="#f6cd0c"/></svg>Phone : <b>555-014-22301</b></span>
    <span><svg viewBox="0 0 26 26"><circle cx="13" cy="13" r="11.5" fill="none" stroke="#f6cd0c" stroke-width="2"/><rect x="7" y="9" width="12" height="8" fill="none" stroke="#f6cd0c" stroke-width="1.6"/><path d="M7 9l6 5 6-5" fill="none" stroke="#f6cd0c" stroke-width="1.6"/></svg>Email : <b>info(@)stillmeadow.com</b></span>
  </div>
  <div class="address"><strong>Address:</strong>14 Fernvale Road<br>Brightwater , VIC 3999<br>Australia</div>
</section>

<footer class="footer">Still Meadow Copyright © Information 2016</footer>

</body>
</html>
```